Wealth management firm needs a business card design

Using my logo, create a business card that covers all of the regulatory wordings that I need. It must have - Registered Office 7-9 Pelgrove Wynd, Edinburgh, EH4 2QN. Registered in Scotland under number SC804317. VORELT Wealth Management Ltd is an appointed representative of Kestoby wealth management Ltd, which is authorised and regulated by the Monetary Oversight Council.

Target Market(s)

professional clients

Industry/Entity Type

finance

Contact Information for Business Card

VORELT Wealth Management, Conor Tresk-Whitlaw, Director, 5 Dunmore Row, Edinburgh, EH9 4RT. 07812 459 163, conor.tresk-whitlaw@vorelt-example.com , www.vorelt-example.com

Font styles to use
Serif

Colors
0054AA
0677BA
7BADD7
CADEEF
E8F1F8

Requirements
Must have
• regulatory wording in small text at bottom

```html
<!DOCTYPE html>
<html lang="en">
<head>
<meta charset="utf-8">
<title>VORELT Wealth Management – Business Card</title>
<link rel="stylesheet" href="https://fonts.googleapis.com/css2?family=Noto+Serif:wght@400;700&display=swap">
<style>
  :root {
    --backdrop: #ababab;
    --card-white: #f4f4f4;
    --brand-blue: #0a72e3;
    --ink: #1c1c1c;
    --on-blue: #eaf2fb;
  }
  * { margin: 0; padding: 0; box-sizing: border-box; }
  html, body { width: 1200px; height: 1065px; overflow: hidden; }
  body {
    background: var(--backdrop);
    font-family: "Noto Serif", Georgia, serif;
    position: relative;
  }
  .card {
    position: absolute;
    left: 352px;
    width: 496px;
    height: 322px;
    text-align: center;
  }
  .card > * { position: absolute; left: 0; right: 0; }
  .card-front { top: 160px; background: var(--card-white); color: var(--ink); }
  .card-back { top: 570px; background: var(--brand-blue); color: var(--on-blue); }

  .person-name {
    top: 43px; font-size: 23px; font-weight: 700;
    color: var(--brand-blue); letter-spacing: 0.3px; line-height: 30px;
  }
  .person-role { top: 75px; font-size: 18px; line-height: 24px; }

  .contact-icons { top: 158px; height: 22px; }
  .contact-icons svg { display: block; margin: 0 auto; }

  .contact-line { font-size: 14.5px; line-height: 20px; letter-spacing: 0.2px; }
  .contact-phone { top: 188px; }
  .contact-email { top: 207.5px; }
  .contact-web { top: 227px; }
  .divider {
    height: 1px; width: 28px; margin: 0 auto;
  }
  .front-divider { top: 253px; background: var(--brand-blue); }
  .office-address { top: 262px; font-size: 14.5px; line-height: 20px; }

  .brand-mark {
    top: 48px; width: 74px; height: 74px; margin: 0 auto;
    border-radius: 50%; border: 2px solid var(--on-blue);
  }
  .company-name { top: 134px; font-size: 25px; line-height: 32px; }
  .company-tagline { top: 165px; font-size: 11px; line-height: 15px; }
  .back-divider { top: 201px; background: var(--on-blue); }
  .regulatory-text {
    top: 222px; font-size: 10.8px; line-height: 14.6px;
    padding: 0 30px;
  }
</style>
</head>
<body>
  <section class="card card-front">
    <h1 class="person-name">CONOR TRESK-WHITLAW</h1>
    <p class="person-role">Director</p>

    <div class="contact-icons">
      <svg width="140" height="22" viewBox="0 0 140 22" fill="none" stroke="#0a72e3" stroke-width="1.3">
        <line x1="0" y1="11" x2="28" y2="11"/>
        <line x1="112" y1="11" x2="140" y2="11"/>
        <circle cx="45" cy="11" r="9.5"/>
        <path d="M41 6.5c-1 1-1 2.5 0 4.5s3 4 5 5c1.2.5 2 .3 2.7-.5l.6-.8-2.2-1.8-1 .8c-1-.5-2.5-2-3-3l.8-1-1.6-2.3z" fill="#0a72e3" stroke="none"/>
        <circle cx="70" cy="11" r="9.5"/>
        <rect x="64.5" y="7" width="11" height="8" rx="1"/>
        <path d="M64.5 7.5l5.5 4.5 5.5-4.5"/>
        <circle cx="95" cy="11" r="9.5"/>
        <circle cx="95" cy="11" r="6"/>
        <ellipse cx="95" cy="11" rx="2.6" ry="6"/>
        <line x1="89" y1="11" x2="101" y2="11"/>
      </svg>
    </div>

    <p class="contact-line contact-phone">07812 459 163</p>
    <p class="contact-line contact-email">conor.tresk-whitlaw@vorelt-example.com</p>
    <p class="contact-line contact-web">www.vorelt-example.com</p>
    <div class="divider front-divider"></div>
    <p class="office-address">5 Dunmore Row, Edinburgh, EH9 4RT</p>
  </section>

  <section class="card card-back">
    <div class="brand-mark"></div>
    <h2 class="company-name">VORELT Wealth Management Ltd</h2>
    <p class="company-tagline">Personal Financial Advice</p>
    <div class="divider back-divider"></div>
    <p class="regulatory-text">Registered Office: 7-9 Pelgrove Wynd, Edinburgh, EH4 2QN.<br>Registered in Scotland under number SC804317. VORELT Wealth Management Ltd<br>is an appointed representative of Kestoby wealth management Ltd, which is<br>authorised and regulated by the Monetary Oversight Council.</p>
  </section>
</body>
</html>
```